Newly created Management Consulting company needs a brochure to capture clients's interest

This is a new management consulting firm providing service in Finance, Marketing, Operations/Manufacturing Strategy, and Project Management.
Please go to the company's website: www.veltanorpartners.ca . The website is pretty straightforward and gives a clear explanation of all the services and sub-services offered. Based on the existent material on the website, I would like to create a company's brochure that can inspire clients to seek our services.
One important thing: the slogan/tagline ("Shaping the future of your business") needs to be added somewhere in the vicinity of our company's' LOGO. Please see attached the company's logo (JPEG file).
The brochure size and number of pages can vary, depending on the layout of the brochure so it can fit the content, so I am open to different and innovative sizes/shapes and no. of pages etc. Graphics should combine real pictures with graphic design technology, and should give a professional look and feel comparable to big companies' marketing materials.
Updates
The brochure does not necessarily have to include pictures that are on the website. If you think that other pictures and graphics can deliver a stronger message to customers, by all means I am open to any other ideas.
Thanks.
As I said before, the pictures do not need to be exactly the same pictures as on the website, if you can bring in other cool pictures to attract clients, please go ahead. Also, you do not need to use only black background, if you have better colors ideas to combine with the our LOGO, and it looks good, by all means do use other colors. But our LOGO needs to be represented as it is on the JPEG I attached.
May the most creative and cool design win! Good luck!
Please ensure that all the content of our website fits into your brochure, including our contact information. It is up to you to come up with the necessary number of pages, design and shape of the brochure, but the text should be clear enough to be read by a normal person without a magnifying glass.
Thank you.
In order to keep the brochure to a reasonable number of pages, I agree that it is not necessary to include 100% all the text that appears on the website. That being said, even if you do not have enough space to include all the background and introduction paragraphs under each service/sub-service, it is still important that the main message for each service/sub-service is being contained in the brochure.
Target Market(s)
Our clients are companies with sizes starting from 10-20 employees and up to large Larkspan 700 companies.
Industry/Entity Type
Management Consulting
Look and feel

```html
<!DOCTYPE html>
<html lang="en">
<head>
<meta charset="utf-8">
<title>Veltanor Partners – Tri-fold Brochure</title>
<link rel="stylesheet" href="https://fonts.googleapis.com/css2?family=Open+Sans:wght@400;600&display=swap">
<style>
:root{
  --lime:#a6ce39;
  --black:#0b0b0b;
  --ink:#141414;
  --white:#ffffff;
  --grey-text:#e6e6e6;
  --page:#e9e9e9;
}
*{box-sizing:border-box;margin:0;padding:0}
html,body{width:1200px;height:1153px;overflow:hidden}
body{background:var(--page);font-family:"Open Sans",Arial,sans-serif;color:var(--white);position:relative}

/* ---------- outside spread ---------- */
.outside{position:absolute;left:240px;top:18px;width:720px;height:594px;display:flex;background:var(--black);box-shadow:0 2px 8px rgba(0,0,0,.25)}
.panel{position:relative;height:100%}
.panel-intro{width:249px;padding:20px 16px 16px 18px}
.panel-intro h2{color:var(--lime);font-weight:400;font-size:16px;line-height:1.12;margin-bottom:3px}
.panel-intro p{font-size:10.6px;line-height:1.5;margin-bottom:14px;color:var(--grey-text)}
.panel-summit{width:267px;background:var(--black)}
.summit-band{position:absolute;left:0;top:0;width:100%;height:392px;background:var(--lime);display:flex;align-items:center;padding-left:18px}
.summit-band p{color:var(--ink);font-size:18px;line-height:1.55}
.climber{position:absolute;left:150px;top:392px;width:117px;height:118px}
.contact{position:absolute;left:18px;top:488px;font-size:8.6px;line-height:1.45;color:var(--grey-text);font-style:normal}
.panel-cover{width:204px}
.brand{position:absolute;top:86px;left:0;width:100%;text-align:center}
.brand-mark{display:block;width:18px;height:18px;border-radius:50%;background:var(--lime);margin:0 auto 12px}
.brand-name{font-size:22px;font-weight:400;letter-spacing:3px;color:var(--white);line-height:1.1}
.tagline{position:absolute;top:228px;left:22px;font-size:16.5px;line-height:1.45;color:var(--white)}
.tagline em{font-style:normal;color:var(--lime)}
.solutions-band{position:absolute;left:0;top:380px;width:100%;height:176px;background:var(--lime);display:flex;align-items:center;justify-content:center;text-align:center}
.solutions-band p{color:var(--ink);font-size:16px;line-height:1.45}

/* ---------- inside spread ---------- */
.inside{position:absolute;left:240px;top:632px;width:720px;height:507px;background:var(--black);box-shadow:0 2px 8px rgba(0,0,0,.25)}
.trim{position:absolute;left:0;width:100%;height:12px;background:var(--lime)}
.trim-top{top:0}
.trim-bottom{bottom:0;height:16px}
.spread-head{position:absolute;top:26px;left:18px;right:18px;display:flex;justify-content:space-between;font-size:24px;font-weight:400;letter-spacing:.5px}
.spread-rule{position:absolute;top:64px;left:18px;right:18px;height:2px;background:linear-gradient(90deg,var(--lime) 0,var(--lime) 20%,transparent 60%,var(--lime) 100%)}
.columns{position:absolute;top:76px;bottom:24px;left:18px;right:18px;display:flex;gap:24px}
.col{flex:1}
.col h3{color:var(--lime);font-weight:400;font-size:14px;line-height:1.3;margin-bottom:3px}
.col p{font-size:8.3px;line-height:1.6;color:var(--grey-text);text-align:justify;margin-bottom:12px}
.photo{display:block;width:150px;height:80px;margin:0 auto 10px}
</style>
</head>
<body>

<section class="outside" aria-label="Brochure outside">
  <div class="panel panel-intro">
    <h2>Rethinking Operations and Manufacturing</h2>
    <p>How can you take your company to the forefront of your industry, improve your bottom line and surpass your competitors? Is it Time to Rethink Your Manufacturing Strategy?</p>
    <h2>Maximize Shareholders Value</h2>
    <p>Is your finance function both effective and efficient? Are your company’s value-drivers linked to value creation? We can help clients not only to assess their financial performance but also to realign their company’s...</p>
    <h2>Unleash the Power of Marketing and Sales</h2>
    <p>From identifying trends and influences to developing effective sales-force and channels arrangements, our solutions in marketing and sales help clients achieve sustainable economic results.</p>
    <h2>Turn Project Management into a Strategic Advantage</h2>
    <p>Beyond the software, techniques and methods, our project managers have the ability to inspire a team to achievement and make tough choices, so that your projects are successfully delivered on time and on budget.</p>
  </div>

  <div class="panel panel-summit">
    <div class="summit-band"><p>Helping you reach<br>the summit</p></div>
    <svg class="climber" role="img" aria-label="Silhouette of a climber reaching the top of a rock" viewBox="0 0 117 118" preserveAspectRatio="none">
      <defs><linearGradient id="rockTone" x1="0" y1="0" x2="0" y2="1"><stop offset="0" stop-color="#1c1c1c"/><stop offset="1" stop-color="#0b0b0b"/></linearGradient></defs>
      <rect width="117" height="118" fill="url(#rockTone)"/>
    </svg>
    <address class="contact">
      Suite 410<br>Harbourline Tower<br>820 Cordell Street<br>Vancouver, BC V6B 2K4<br>Canada<br>E: info@veltanorpartners.ca<br>P: 778-555-0142<br>W: www.veltanorpartners.ca
    </address>
  </div>

  <div class="panel panel-cover">
    <div class="brand">
      <span class="brand-mark"></span>
      <div class="brand-name">VELTANOR<br>PARTNERS</div>
    </div>
    <p class="tagline">shaping the future of<br><em>YOUR</em> business</p>
    <div class="solutions-band"><p>Strategic and Analytic<br>Management Solutions</p></div>
  </div>
</section>

<section class="inside" aria-label="Brochure inside">
  <div class="trim trim-top"></div>
  <div class="spread-head"><span>ABOUT</span><span>SERVICES</span></div>
  <div class="spread-rule"></div>
  <div class="columns">
    <div class="col">
      <p>Veltanor Partners chief focus is addressing the critical business challenges of our clients. We work across all industries and guide our customers in making the right decisions and conducting the best course of action in operations, marketing, and finance. We come up with solutions for a company that will improve performance, reduce costs and maximize growth. Our dedicated, professional team consists of MBAs and engineers of high standing with a variety of educational and industry experiences. They bring their intelligence and analytical skills to every client. Above all, they are passionate about taking on new challenges and share a deep commitment to excellence.</p>
      <h3>Our approach</h3>
      <p>The way we conduct business at Veltanor Partners backs up these aspirations. Our fees are based on the value we create for our clients. We only work on a project basis and we work collaboratively with our clients. Veltanor Partners is not a firm that is just going to conduct studies to illustrate a client’s challenges. We deliver lasting, measurable results.</p>
    </div>
    <div class="col">
      <h3>Finance</h3>
      <p>Veltanor Partners can support and advise clients in a variety of industries with their strategic and corporate finance issues in order to maximize shareholder value. Our consultants take a holistic view of the corporate finance and use data-driven cases to help companies understand their sources of valuation advantage and increase returns to shareholders.</p>
      <svg class="photo" role="img" aria-label="Photo of consultants reviewing financial documents" viewBox="0 0 150 80" preserveAspectRatio="none">
        <defs><linearGradient id="financeTone" x1="0" y1="0" x2="1" y2="1"><stop offset="0" stop-color="#f2f2f2"/><stop offset="1" stop-color="#8a93a0"/></linearGradient></defs>
        <rect width="150" height="80" fill="url(#financeTone)"/>
      </svg>
      <h3>Marketing</h3>
      <p>We, at Veltanor Partners, believe that a holistic marketing approach will help your company succeed in managing a competitive value chain, one that delivers your services and products more efficiently and at a high level of quality. Veltanor consultants use a holistic marketing concept, which takes into account your entire organization and all the key stakeholders including the customers, employees, suppliers, shareholders, the community and the environment.</p>
    </div>
    <div class="col">
      <h3>Operations</h3>
      <p>We work closely with clients of all levels - from small business owners to large corporations. Together, we develop solid operations strategies that will develop resources and configure processes, achieving the competitive position the firm is seeking over time. Our consultants will use their industry experience, rigorous analytical capabilities, and a pragmatic mindset to provide a 360-degree perspective on your operations.</p>
      <svg class="photo" role="img" aria-label="Photo of a hand drawing a process flow chart" viewBox="0 0 150 80" preserveAspectRatio="none">
        <defs><linearGradient id="operationsTone" x1="0" y1="0" x2="1" y2="1"><stop offset="0" stop-color="#ffffff"/><stop offset="1" stop-color="#b9bcc0"/></linearGradient></defs>
        <rect width="150" height="80" fill="url(#operationsTone)"/>
      </svg>
      <h3>Project Management</h3>
      <p>Veltanor Partners helps clients with managing their portfolio of projects. This enables them to successfully complete their strategic projects on time, within budget, and at a high level of quality. We provide our clients with a full-time or part-time resource to help with business or technical projects. Before spending money on your critical and complex ventures, be sure that you have a detailed project management plan in place.</p>
    </div>
  </div>
  <div class="trim trim-bottom"></div>
</section>

</body>
</html>
```